Business Card Design Project

Business card for new event planning company. I will load in 2 different colors of logs for you to use.

Target Market(s)

meeting planners and business leaders

Industry/Entity Type

Event Planning

Requirements
Must have
• memorable/ creative please - maybe logo on back of the card

Information for business card: (Information may change)

LaVonna Birchwell
lav@MarigoldOccasionsandGatherings.com
www.MarigoldOccasionsandGatherings.com
555.730.2964
Nice to have
• Do you think it would be too much to add twiiter, FB, linked in logo to card to connect?

all are LaVonna Birchwell

```html
<!DOCTYPE html>
<html lang="en">
<head>
<meta charset="utf-8">
<title>Marigold Occasions &amp; Gatherings — Business Card</title>
<link rel="stylesheet" href="https://fonts.googleapis.com/css2?family=Arimo:wght@400&display=swap">
<style>
  :root {
    --page: #ffffff;
    --card-red: #e0332a;
    --panel-dark: #2e2d31;
    --brand-lavender: #8c80c9;
    --text-light: #ffffff;
  }
  html, body {
    margin: 0;
    padding: 0;
    width: 1200px;
    height: 900px;
    overflow: hidden;
    background: var(--page);
  }
  .canvas {
    position: relative;
    width: 1200px;
    height: 900px;
  }
  .card {
    position: absolute;
    left: 68px;
    top: 124px;
    width: 1064px;
    height: 652px;
    background: var(--card-red);
    overflow: hidden;
  }
  .brand-panel {
    position: absolute;
    left: 364px;
    top: 228px;
    right: 0;
    bottom: 0;
    background: var(--panel-dark);
    border-top-left-radius: 26px;
    box-shadow: -4px -4px 14px rgba(0, 0, 0, 0.18);
  }
  .brand-lockup {
    position: absolute;
    left: 160px;
    top: 68px;
    display: flex;
    align-items: center;
    gap: 18px;
    font-family: "Arimo", Arial, sans-serif;
    font-weight: 400;
    color: var(--brand-lavender);
  }
  .brand-mark {
    width: 26px;
    height: 26px;
    border-radius: 50%;
    background: var(--brand-lavender);
    flex: none;
  }
  .brand-name {
    display: flex;
    flex-direction: column;
    line-height: 1;
  }
  .brand-name__main {
    font-size: 64px;
  }
  .brand-name__sub {
    font-size: 24px;
    margin-top: 8px;
  }
  .contact-tab {
    position: absolute;
    left: 12px;
    top: 292px;
    right: 0;
    bottom: 0;
    background: var(--card-red);
    border-top-left-radius: 30px;
    box-shadow: -6px -6px 16px rgba(0, 0, 0, 0.35);
  }
  .website {
    position: absolute;
    left: 72px;
    top: 28px;
    margin: 0;
    font-family: "Arimo", Arial, sans-serif;
    font-size: 28px;
    font-weight: 400;
    color: var(--text-light);
    letter-spacing: 0.2px;
  }
</style>
</head>
<body>
  <main class="canvas">
    <section class="card" aria-label="Business card">
      <div class="brand-panel">
        <div class="brand-lockup">
          <span class="brand-mark" aria-hidden="true"></span>
          <div class="brand-name">
            <span class="brand-name__main">Marigold</span>
            <span class="brand-name__sub">Occasions &amp; Gatherings</span>
          </div>
        </div>
        <div class="contact-tab">
          <p class="website">www.MarigoldOccasionsandGatherings.com</p>
        </div>
      </div>
    </section>
  </main>
</body>
</html>
```